Business Cards and label design needed!

I am a metalsmith, working in sterling silver, brass and moving slowly into adding some gold accent pieces. I also use patinas to add color to brass pieces. The peacock feather is used in my packaging, as both a label and tissue paper. I am attaching what I am currently using, and printing at home, but I need a design that I can have professionally printed. My website is www.willowharborcrafts.com
Target Market(s)
Established Professionals, Independent thinkers, Art donors, Artist supporters
Industry/Entity Type
Jewelry
Contact Information for Business Card
I would like a business card with the basic contact information, including Facebook and Instagram. I currently use a peacock feather and would like to continue that. I like to use turquoise, Tiffany blue and colors in that direction. I am open to other suggestions. I would like to be able to transfer the design to oval labels as well.
Font styles to use
Other font styles liked:
- Garamond or other fonts that have a slight script that is easy to read
Look and feel

```html
<!DOCTYPE html>
<html lang="en">
<head>
<meta charset="utf-8">
<title>Willow Harbor Crafts — Business Card</title>
<link href="https://fonts.googleapis.com/css2?family=Playfair+Display&family=Montserrat:wght@400;700&display=swap" rel="stylesheet">
<style>
  :root {
    --backdrop: #ececec;
    --card-white: #f7f7f7;
    --teal: #249a94;
    --ink-grey: #5c5c5c;
    --feather-tan: #c4a676;
    --feather-olive: #8d8a5c;
    --oval-white: #f3f3f3;
  }
  * { margin: 0; padding: 0; box-sizing: border-box; }
  html, body { width: 1200px; height: 1098px; overflow: hidden; background: var(--backdrop); }
  .canvas { position: relative; width: 1200px; height: 1098px; }
  .card {
    position: absolute; left: 220px; width: 760px; height: 434px;
    box-shadow: 0 6px 18px rgba(0,0,0,0.12);
  }
  .card--front { top: 90px; background: var(--card-white); }
  .card--back { top: 574px; background: var(--teal); }

  .feather {
    border-radius: 40%;
    background: linear-gradient(135deg, rgba(196,166,118,0.35), var(--feather-tan) 45%, var(--feather-olive) 80%, rgba(141,138,92,0.5));
  }
  .card--front .feather { position: absolute; left: 56px; top: 40px; width: 96px; height: 72px; }

  .brand-name {
    font-family: "Playfair Display", serif;
    font-weight: 400; color: var(--teal);
    white-space: nowrap; line-height: 1.1;
  }
  .card--front .brand-name { position: absolute; left: 200px; top: 126px; font-size: 44px; }

  .contact { position: absolute; left: 150px; top: 205px; font-family: "Montserrat", sans-serif; color: var(--ink-grey); }
  .contact__person { font-weight: 700; font-size: 30px; margin-left: 150px; margin-bottom: 4px; }
  .contact__person .surname { letter-spacing: 0.5px; }
  .contact__line { display: flex; align-items: center; gap: 10px; font-size: 22px; line-height: 1.45; }
  .contact__line--phone { margin-left: 150px; }
  .contact__line svg { width: 18px; height: 18px; flex: none; }

  .label-oval {
    position: absolute; left: 120px; top: 77px; width: 520px; height: 280px;
    border-radius: 50%; background: var(--oval-white);
    display: flex; flex-direction: column; align-items: center; justify-content: center; gap: 14px;
  }
  .label-oval .feather { width: 110px; height: 70px; }
  .label-oval .brand-name { font-size: 42px; }
</style>
</head>
<body>
<div class="canvas">
  <section class="card card--front">
    <div class="feather" role="img" aria-label="Peacock feather illustration"></div>
    <div class="brand-name">Willow Harbor Crafts</div>
    <div class="contact">
      <div class="contact__person">Maren <span class="surname">HOLT</span></div>
      <div class="contact__line contact__line--phone">
        <svg viewBox="0 0 24 24" aria-hidden="true"><path fill="var(--teal)" d="M6.6 10.8a15 15 0 0 0 6.6 6.6l2.2-2.2a1 1 0 0 1 1-.25 11.4 11.4 0 0 0 3.6.6 1 1 0 0 1 1 1V20a1 1 0 0 1-1 1A17 17 0 0 1 3 4a1 1 0 0 1 1-1h3.5a1 1 0 0 1 1 1c0 1.25.2 2.45.6 3.6a1 1 0 0 1-.25 1z"/></svg>
        <span>555.012.3478</span>
      </div>
      <div class="contact__line">
        <svg viewBox="0 0 24 24" aria-hidden="true"><rect x="2.5" y="5" width="19" height="14" fill="none" stroke="var(--teal)" stroke-width="2"/><path d="M2.5 5l9.5 8 9.5-8" fill="none" stroke="var(--teal)" stroke-width="2"/></svg>
        <span>designsbywillowharbor@mail.com</span>
      </div>
      <div class="contact__line">
        <svg viewBox="0 0 24 24" aria-hidden="true"><g fill="none" stroke="var(--teal)" stroke-width="1.8"><circle cx="12" cy="12" r="9.5"/><ellipse cx="12" cy="12" rx="4.5" ry="9.5"/><path d="M2.5 12h19M4 7h16M4 17h16"/></g></svg>
        <span>www.willowharborcrafts.com</span>
      </div>
    </div>
  </section>

  <section class="card card--back">
    <div class="label-oval">
      <div class="feather" role="img" aria-label="Peacock feather illustration"></div>
      <div class="brand-name">Willow Harbor Crafts</div>
    </div>
  </section>
</div>
</body>
</html>
```